Business Card Design

We have recently seen two business cards that caught our attention and think the designs would work for us. We are an accounting firm that serves small businesses in a variety of industries. Attached are the two business card that inspired us along with very rough layouts. We would like to see a professional layout using our company information.

Industry/Entity Type

Accounting

Contact Information for Business Card

Company Name - Porter Lyle
Address - 4120 Marbury Lane, Suite 310, Houston, TX 77058
713-555-0186 - Main
281-555-0143 - Fax

Team Member Names, emails and phone numbers (see attachment)

```html
<!DOCTYPE html>
<html lang="en">
<head>
<meta charset="utf-8">
<title>Porter Lyle – Business Card</title>
<link rel="stylesheet" href="https://fonts.googleapis.com/css2?family=Crimson+Pro:wght@400;500&display=swap">
<style>
  :root {
    --backdrop: #e9e7e3;
    --card: #ffffff;
    --ink: #1f1f1f;
    --ink-soft: #3d3d3f;
    --grey-light: #b3b4b6;
    --grey-mid: #939598;
    --label: #8a8b8d;
    --white: #ffffff;
  }
  * { margin: 0; padding: 0; box-sizing: border-box; }
  html, body {
    width: 1200px; height: 1000px; overflow: hidden;
    background: var(--backdrop);
    font-family: "Crimson Pro", Georgia, serif;
  }
  .card {
    position: absolute; left: 150px; top: 243px;
    width: 900px; height: 514px;
    background: var(--card);
    box-shadow: 0 10px 28px rgba(0,0,0,0.18);
    overflow: hidden;
  }
  .decor-left {
    position: absolute; left: 0; top: 236px; width: 455px; height: 278px;
    background: linear-gradient(180deg, var(--grey-light), var(--grey-mid));
  }
  .decor-right {
    position: absolute; left: 600px; top: 430px; width: 300px; height: 84px;
    background: linear-gradient(180deg, var(--grey-light), var(--grey-mid));
  }
  .divider {
    position: absolute; left: 448px; top: 222px; width: 3px; height: 248px;
    background: var(--ink);
  }

  .member { position: absolute; left: 20px; top: 286px; width: 410px; text-align: right; }
  .member-name { font-size: 50px; font-weight: 400; color: var(--ink-soft); line-height: 1; white-space: nowrap; }
  .member-title { font-size: 21px; color: var(--white); margin-top: 6px; }

  .brand { position: absolute; left: 490px; top: 56px; display: flex; flex-direction: column; align-items: flex-start; }
  .brand-mark { width: 92px; height: 92px; background: var(--ink); margin: 0 0 18px 40px; }
  .brand-name { font-size: 38px; font-weight: 500; color: var(--ink); line-height: 1; letter-spacing: 0.5px; }

  .contact { position: absolute; left: 492px; top: 252px; color: var(--ink-soft); font-size: 21px; line-height: 1.3; }
  .address { margin-bottom: 10px; }
  .phone-label { color: var(--label); }
</style>
</head>
<body>
  <div class="card">
    <div class="decor-left" role="img" aria-label="Grey folded ribbon decoration"></div>
    <div class="decor-right" role="img" aria-label="Grey folded ribbon decoration"></div>
    <div class="divider"></div>

    <div class="member">
      <div class="member-name">Marisa Dalton</div>
      <div class="member-title">Account Manager</div>
    </div>

    <div class="brand">
      <div class="brand-mark"></div>
      <div class="brand-name">Porter Lyle</div>
    </div>

    <div class="contact">
      <div class="address">4120 Marbury Lane, Suite 310<br>Houston, TX 77058</div>
      <div>713-555-0186 – <span class="phone-label">Main</span></div>
      <div>713-555-0172 – <span class="phone-label">Direct</span></div>
      <div>832-555-0119 - <span class="phone-label">Mobile</span></div>
    </div>
  </div>
</body>
</html>
```